BRIX Rentals ( Website Graphic design ) small property management new business ( real estate )

I need a website designed for a new small Property Management ( no sales ) company I'm starting up soon. I have a design in mind that I like and would like to keep it quite similar to this if possible using my logo and colour scheme and slightly ALTER the layout. and maybe a little more interactive with some motion and images etc
Please see the link to show the simplicity I'm after. I want to be bold ad very clear and concise. I love the simplicity of this design but not necessarily the pages with just text on them. I would want them to be a bit more interesting with some pictures and photos. http://www.lindavostrel.com.au/

The branding on the site should be bold and very sharp.

My target market is the mid to high end of the rental market in Darwin Australia and should reflect "good quality, outstanding service and attention to detail, energetic, integrity, "

I will only require a few pages to start with, Home / Company Profile / Management Services / Owners information / Tenant information / Properties and About Darwin. I will be able to provide text for each of the pages but would be no more than 4-6 paragraphs apart from the management services page which would detail a number of the services we would offer. The properties page will just be a link to homelistz,com.au to show my listings and then a couple more links to owner and tenant portals, chatterbox page etc. It must also be responsive to mobile devices.

I would also like to include a chatterbox page design and build.

regards
Marta Penhale

Target Market(s)

property owners, investors, Darwin Australia, renters, ages 30 - 60, tenants

Industry/Entity Type

Property Management

Font styles to use
Other font styles liked:
• i like helvetica, but not essential

Requirements
Must have
• Clean and crisp pages, not busy , responsive to devices
• links to portals and chatterbox, any ability to add other links at a later date.
Nice to have
• music - must be upbeat but not over the top
Should not have
• be too busy on each page

```html
<!DOCTYPE html>
<html lang="en">
<head>
<meta charset="utf-8">
<title>BRIX Rentals – Property Management Darwin</title>
<link href="https://fonts.googleapis.com/css2?family=Open+Sans:wght@400;600;700&family=Oswald:wght@400;500&display=swap" rel="stylesheet">
<style>
:root{
  --teal:#1e8a93;
  --teal-dark:#17666d;
  --nav:#2d7179;
  --ink:#2b2b2b;
  --text:#6b6b6b;
  --muted:#9a9a9a;
  --band:#f1f1f1;
  --line:#dcdcdc;
  --footer:#323232;
  --footer-bottom:#242424;
  --white:#ffffff;
}
*{box-sizing:border-box;margin:0;padding:0}
html,body{width:747px;height:1200px;overflow:hidden;background:var(--white)}
body{font-family:"Open Sans",Arial,sans-serif;color:var(--text);position:relative}
.wrap{width:637px;margin:0 auto;position:relative}

/* header */
.site-header{height:84px;display:flex;align-items:center;justify-content:center}
.brand{display:flex;align-items:center;gap:8px;font-family:"Open Sans",Arial,sans-serif;font-weight:700;font-size:18px;color:var(--ink)}
.brand-mark{width:16px;height:16px;background:var(--ink)}

/* navigation */
.main-nav{height:26px;background:linear-gradient(var(--nav),var(--teal-dark));display:flex}
.main-nav a{color:var(--white);text-decoration:none;font-size:7px;font-weight:700;letter-spacing:.3px;text-transform:uppercase;padding:0 12px;line-height:26px;white-space:nowrap}
.main-nav a.active{background:var(--ink)}

/* hero */
.hero{height:345px;position:relative;background:linear-gradient(180deg,#6fa6d8 0%,#a9cdea 35%,#7f97a8 60%,#4d6270 80%,#3d5a3a 100%)}
.hero-caption{position:absolute;left:50%;transform:translateX(-50%);top:258px;width:370px;background:rgba(20,20,20,.7);text-align:center;padding:7px 10px 8px;color:var(--white)}
.hero-caption h1{font-family:"Oswald",Arial,sans-serif;font-weight:400;font-size:15px;letter-spacing:1px}
.hero-caption p{font-size:6.5px;color:#ddd;margin-top:2px}
.hero-dots{position:absolute;top:316px;left:50%;transform:translateX(-50%);display:flex;gap:4px}
.hero-dots span{width:6px;height:6px;border-radius:50%;border:1px solid var(--white)}
.hero-dots span.on{background:var(--white)}

/* features */
.features{display:flex;gap:22px;padding:18px 10px 0;height:108px}
.feature{flex:1;display:flex;gap:8px}
.feature-icon{flex:none;width:30px;height:30px;border:1.5px solid var(--ink);border-radius:50%;display:flex;align-items:center;justify-content:center}
.feature h3{color:var(--teal);font-size:7.5px;font-weight:700;text-transform:uppercase;margin:4px 0 3px}
.feature p{font-size:6px;line-height:1.5}

/* feature properties */
.feature-band{background:var(--band);border-top:1px solid var(--line);height:240px;padding-top:26px}
.section-title{display:flex;align-items:center;gap:12px;justify-content:center;font-family:"Oswald",Arial,sans-serif;font-size:13px;color:var(--ink);letter-spacing:1.5px;text-transform:uppercase}
.section-title::before,.section-title::after{content:"";flex:1;height:1px;background:#bdbdbd}
.properties{display:flex;gap:12px;margin-top:22px}
.property{flex:1;background:var(--white);border:1px solid var(--line)}
.property-photo{height:118px}
.property-info{display:flex;justify-content:space-between;align-items:center;padding:9px 7px;font-size:6.5px}
.property-info .place{display:flex;align-items:center;gap:3px}
.property-info .price{font-size:9px;font-weight:700;color:var(--ink)}

/* columns */
.columns{display:flex;gap:22px;padding-top:18px;height:205px}
.col{flex:1}
.col h2{font-family:"Oswald",Arial,sans-serif;font-weight:400;font-size:11px;color:var(--ink);text-transform:uppercase;letter-spacing:.6px;border-bottom:1px solid var(--line);padding-bottom:5px;margin-bottom:9px}
.list-item{display:flex;gap:7px;margin-bottom:9px}
.thumb{flex:none;width:38px;height:28px}
.list-item h4{font-size:6.5px;color:var(--teal);font-weight:700;text-transform:uppercase}
.list-item p{font-size:5.5px;line-height:1.4}
.list-item a{font-size:5.5px;color:var(--ink);font-weight:600;text-decoration:none}
.profile-photo{height:80px;margin-bottom:8px}
.col p.body{font-size:6px;line-height:1.55;margin-bottom:5px}

/* footer */
.site-footer{position:absolute;left:0;right:0;top:1008px;height:162px;background:var(--footer);color:#bbb}
.footer-cols{display:flex;gap:30px;padding-top:14px}
.footer-cols h5{font-size:7.5px;color:var(--white);text-transform:uppercase;font-weight:700;margin-bottom:8px;letter-spacing:.4px}
.footer-cols p{font-size:6.5px;line-height:1.6}
.f-contact{flex:1}
.f-news{flex:1.1}
.f-follow{flex:.6}
.newsletter{display:flex;margin-top:4px}
.newsletter span{width:110px;height:18px;background:var(--white);color:var(--muted);font-size:6.5px;line-height:18px;padding-left:5px}
.newsletter b{height:18px;background:var(--teal);color:var(--white);font-size:6.5px;line-height:18px;padding:0 8px}
.socials{display:flex;gap:5px}
.socials span{width:15px;height:15px;border:1.5px solid #ccc;border-radius:50%}
.footer-bottom{position:absolute;left:0;right:0;top:1170px;height:30px;background:var(--footer-bottom);color:#999;font-size:6.5px;text-align:center;line-height:30px}
</style>
</head>
<body>

<header class="site-header">
  <div class="brand"><span class="brand-mark"></span>BRIX Rentals</div>
</header>

<div class="wrap">
  <nav class="main-nav">
    <a class="active">Home</a>
    <a>Company Profile</a>
    <a>Management Services</a>
    <a>Owners Information</a>
    <a>Tenant Information</a>
    <a>Properties</a>
    <a>About Darwin</a>
  </nav>

  <section class="hero" role="img" aria-label="City skyline of glass towers under a blue sky">
    <div class="hero-caption">
      <h1>WELCOME TO BRIX RENTALS</h1>
      <p>Quality rental homes managed with care, clear service and close attention to every detail.</p>
    </div>
    <div class="hero-dots"><span class="on"></span><span></span><span></span><span></span></div>
  </section>

  <section class="features">
    <div class="feature">
      <div class="feature-icon"><svg width="14" height="14" viewBox="0 0 14 14"><path d="M2 7 L7 2.5 L12 7 M3.5 6 V12 H10.5 V6" fill="none" stroke="#2b2b2b" stroke-width="1.3"/></svg></div>
      <div><h3>Eque Porro Quisquam</h3><p>It is a long established fact that a tenant will be reassured by the readable content of a page when looking at its layout.</p></div>
    </div>
    <div class="feature">
      <div class="feature-icon"><svg width="14" height="14" viewBox="0 0 14 14"><rect x="2" y="3" width="10" height="6.5" fill="none" stroke="#2b2b2b" stroke-width="1.2"/><path d="M5 12 H9 M7 9.5 V12" stroke="#2b2b2b" stroke-width="1.2"/></svg></div>
      <div><h3>Eque Porro Quisquam</h3><p>It is a long established fact that an owner will be reassured by the readable content of a page when looking at its layout.</p></div>
    </div>
    <div class="feature">
      <div class="feature-icon"><svg width="14" height="14" viewBox="0 0 14 14"><path d="M3 11 L11 3 M3 3 L11 11" stroke="#2b2b2b" stroke-width="1.4"/><circle cx="3" cy="3" r="1.4" fill="#2b2b2b"/><circle cx="11" cy="3" r="1.4" fill="#2b2b2b"/></svg></div>
      <div><h3>Eque Porro Quisquam</h3><p>It is a long established fact that a reader will be reassured by the readable content of a page when looking at its layout.</p></div>
    </div>
  </section>
</div>

<section class="feature-band">
  <div class="wrap">
    <h2 class="section-title">Feature Properties</h2>
    <div class="properties">
      <article class="property">
        <div class="property-photo" role="img" aria-label="Harbour foreshore with modern buildings" style="background:linear-gradient(180deg,#8fb7d9,#5f8aa0 60%,#3f6b57)"></div>
        <div class="property-info"><span class="place"><svg width="6" height="8" viewBox="0 0 6 8"><path d="M3 8 L0.6 4 A2.6 2.6 0 1 1 5.4 4 Z" fill="#2b2b2b"/></svg>Darwin, Australia</span><span class="price">$37.00</span></div>
      </article>
      <article class="property">
        <div class="property-photo" role="img" aria-label="Tall landmark tower against a pale sky" style="background:linear-gradient(180deg,#c9dbe9,#8da6b8 55%,#6b7f6a)"></div>
        <div class="property-info"><span class="place"><svg width="6" height="8" viewBox="0 0 6 8"><path d="M3 8 L0.6 4 A2.6 2.6 0 1 1 5.4 4 Z" fill="#2b2b2b"/></svg>Darwin, Australia</span><span class="price">$37.00</span></div>
      </article>
      <article class="property">
        <div class="property-photo" role="img" aria-label="City skyline at dusk" style="background:linear-gradient(180deg,#d9c9b8,#9a8f8a 50%,#4e5a6a)"></div>
        <div class="property-info"><span class="place"><svg width="6" height="8" viewBox="0 0 6 8"><path d="M3 8 L0.6 4 A2.6 2.6 0 1 1 5.4 4 Z" fill="#2b2b2b"/></svg>Darwin, Australia</span><span class="price">$37.00</span></div>
      </article>
      <article class="property">
        <div class="property-photo" role="img" aria-label="Waterfront buildings under a cloudy sky" style="background:linear-gradient(180deg,#7aa3c8,#a9bfcf 45%,#5d7787)"></div>
        <div class="property-info"><span class="place"><svg width="6" height="8" viewBox="0 0 6 8"><path d="M3 8 L0.6 4 A2.6 2.6 0 1 1 5.4 4 Z" fill="#2b2b2b"/></svg>Darwin, Australia</span><span class="price">$37.00</span></div>
      </article>
    </div>
  </div>
</section>

<div class="wrap">
  <section class="columns">
    <div class="col">
      <h2>Management Services</h2>
      <div class="list-item"><div class="thumb" role="img" aria-label="Office tower" style="background:linear-gradient(#7ea3c4,#4d6a80)"></div><div><h4>Neque Porro Quisquam Est</h4><p>A long established fact that a reader will find a listing at its layout.</p><a>Read More</a></div></div>
      <div class="list-item"><div class="thumb" role="img" aria-label="Apartment block" style="background:linear-gradient(#9bb8cf,#60788a)"></div><div><h4>Neque Porro Quisquam Est</h4><p>A long established fact that a reader will find a listing at its layout.</p><a>Read More</a></div></div>
      <div class="list-item"><div class="thumb" role="img" aria-label="Street of houses" style="background:linear-gradient(#8fae9a,#4e6a55)"></div><div><h4>Neque Porro Quisquam Est</h4><p>A long established fact that a reader will find a listing at its layout.</p><a>Read More</a></div></div>
      <div class="list-item"><div class="thumb" role="img" aria-label="Modern home exterior" style="background:linear-gradient(#b5c4cf,#6f7f8a)"></div><div><h4>Neque Porro Quisquam Est</h4><p>A long established fact that a reader will find a listing at its layout.</p><a>Read More</a></div></div>
    </div>
    <div class="col">
      <h2>Company Profile</h2>
      <div class="profile-photo" role="img" aria-label="City skyline beside parkland" style="background:linear-gradient(180deg,#a7c6e2,#7894aa 55%,#4f7048)"></div>
      <p class="body">It is a long established fact that a reader will be reassured by the readable content of a page when looking at its layout. The point of using local care is that renters and owners alike receive steady attention.</p>
      <p class="body">This point of using a team is that it has a more-or-less normal flow of clear letters, making it look like readable English.</p>
    </div>
    <div class="col">
      <h2>Owners Information</h2>
      <div class="list-item"><div class="thumb" role="img" aria-label="Portrait photo of an owner" style="background:linear-gradient(#c9b7a6,#6f6460)"></div><div><h4>Neque Porro Quisquam Est</h4><p>A long established fact that a reader will find a listing at its layout.</p><a>Click Here</a></div></div>
      <div class="list-item"><div class="thumb" role="img" aria-label="Portrait photo of an owner" style="background:linear-gradient(#b8a99c,#5d5650)"></div><div><h4>Neque Porro Quisquam Est</h4><p>A long established fact that a reader will find a listing at its layout.</p><a>Click Here</a></div></div>
      <div class="list-item"><div class="thumb" role="img" aria-label="Portrait photo of an owner" style="background:linear-gradient(#c2b4a8,#68605a)"></div><div><h4>Neque Porro Quisquam Est</h4><p>A long established fact that a reader will find a listing at its layout.</p><a>Click Here</a></div></div>
      <div class="list-item"><div class="thumb" role="img" aria-label="Portrait photo of an owner" style="background:linear-gradient(#a9a3a0,#4f4c4b)"></div><div><h4>Neque Porro Quisquam Est</h4><p>A long established fact that a reader will find a listing at its layout.</p><a>Click Here</a></div></div>
    </div>
  </section>
</div>

<footer class="site-footer">
  <div class="wrap footer-cols">
    <div class="f-contact">
      <h5>Contact Us</h5>
      <p>BRIX Rentals Pty Ltd, 18 Mitchell Lane,<br>Darwin NT 0800</p>
      <p style="margin-top:6px">(08) 7100 4826<br>hello@brixrentals.example</p>
    </div>
    <div class="f-news">
      <h5>Newsletter</h5>
      <div class="newsletter"><span>Email</span><b>SUBSCRIBE</b></div>
    </div>
    <div class="f-follow">
      <h5>Follow Us</h5>
      <div class="socials"><span></span><span></span><span></span><span></span></div>
    </div>
  </div>
</footer>
<div class="footer-bottom">Copyright © 2014 BRIX Rentals, all rights are reserved.</div>

</body>
</html>
```